I need a label design to go on our jars of honey. Our company is called Quillbrook Honey Co. The type of honey is called Marram Glade Honey. The jars are 1kg. Attached is the label size. Left hand side needs to have nutritional info... as attached. Middle section is our company name, honey type, 1kg & Whangamata, NZ. Right hand side needs to have info as per photo (raw honey etc). I would like to upload more pictures... but I’m unsure how to do this? Thanks, Noreen

Target Market(s)

Honey consumers... families

Industry/Entity Type

Food Production

Colors

Designer to choose colors to be used in the design.

Requirements
Must have
• Nutritional info as per upload
• Type of honey & company name as per upload
• 1kg
• Address
Nice to have
• Similar fonts to upload.
• Possibly background image... floral or beach... very faint though.

```html
<!DOCTYPE html>
<html lang="en">
<head>
<meta charset="utf-8">
<title>Quillbrook Honey Co. – Marram Glade Honey jar label</title>
<link rel="stylesheet" href="https://fonts.googleapis.com/css2?family=Amatic+SC:wght@400&family=Barlow+Condensed:wght@400&family=Caveat:wght@400&family=Dancing+Script:wght@600&display=swap">
<style>
  :root {
    --backdrop: #3a3a3c;
    --label-pink: #ec83b5;
    --ink-white: #ffffff;
    --script-magenta: #a01858;
    --bloom-pink: #f4a9cc;
    --bloom-cream: #fbe3c8;
  }
  html, body {
    margin: 0;
    padding: 0;
    width: 1200px;
    height: 669px;
    overflow: hidden;
    background: var(--backdrop);
  }
  .canvas {
    position: relative;
    width: 1200px;
    height: 669px;
    color: var(--ink-white);
  }
  .label-shape {
    position: absolute;
    inset: 0;
  }
  .floral-band {
    position: absolute;
    left: 430px;
    top: 70px;
    width: 350px;
    height: 128px;
    border-radius: 50%;
    background: radial-gradient(ellipse at 42% 45%, var(--bloom-cream) 0%, var(--bloom-pink) 40%, rgba(244,169,204,0.5) 68%, rgba(236,131,181,0) 100%);
  }

  /* Left column: story */
  .story {
    position: absolute;
    left: 92px;
    width: 276px;
    top: 217px;
    text-align: center;
    font-family: "Caveat", cursive;
    font-size: 19px;
    line-height: 20px;
  }
  .story p { margin: 0 0 25px; }
  .story .contact { margin-top: 18px; }

  /* Centre column: brand */
  .brand {
    position: absolute;
    left: 380px;
    width: 440px;
    text-align: center;
    margin: 0;
  }
  .brand-name {
    top: 236px;
    font-family: "Barlow Condensed", sans-serif;
    font-weight: 400;
    font-size: 40px;
    line-height: 48px;
    letter-spacing: 1px;
  }
  .honey-type {
    top: 322px;
    font-family: "Dancing Script", cursive;
    font-weight: 600;
    color: var(--script-magenta);
    font-size: 92px;
    line-height: 88px;
  }
  .net-weight {
    top: 518px;
    font-family: "Amatic SC", sans-serif;
    font-size: 24px;
  }
  .origin {
    top: 550px;
    font-family: "Amatic SC", sans-serif;
    font-size: 26px;
    letter-spacing: 2px;
  }

  /* Right column: facts */
  .facts {
    position: absolute;
    left: 830px;
    width: 268px;
    text-align: center;
    font-family: "Barlow Condensed", sans-serif;
    margin: 0;
  }
  .claims { top: 216px; font-size: 19px; line-height: 20px; }
  .nutrition-panel {
    position: absolute;
    left: 850px;
    top: 264px;
    width: 226px;
    height: 243px;
    border: 2px solid var(--ink-white);
    box-sizing: border-box;
    font-family: "Barlow Condensed", sans-serif;
  }
  .nutrition-panel .rule {
    position: absolute;
    left: 0;
    right: 0;
    border-top: 2px solid var(--ink-white);
  }
  .rule-serving { top: 62px; }
  .rule-heads { top: 116px; }
  .nutrition-title {
    position: absolute;
    left: 7px;
    top: 2px;
    margin: 0;
    font-size: 22px;
    line-height: 26px;
    font-weight: 400;
    white-space: nowrap;
  }
  .serving {
    position: absolute;
    left: 7px;
    top: 27px;
    font-size: 15px;
    line-height: 16px;
    white-space: nowrap;
  }
  .col {
    position: absolute;
    font-size: 15px;
    line-height: 16px;
    white-space: nowrap;
  }
  .col-head { top: 70px; line-height: 14.5px; }
  .col-body { top: 128px; }
  .col-label { left: 7px; }
  .col-serving { left: 91px; }
  .col-100g { left: 163px; }
  .storage { top: 516px; font-size: 16px; line-height: 16px; }
</style>
</head>
<body>
<div class="canvas">
  <svg class="label-shape" width="1200" height="669" viewBox="0 0 1200 669" aria-hidden="true">
    <path d="M77 190 H366 A273 273 0 0 1 834 190 H1123 V608 H77 Z" fill="var(--label-pink)"/>
  </svg>

  <div class="floral-band" role="img" aria-label="Watercolour spray of pink, cream and yellow flowers with green leaves across the top of the arch"></div>

  <div class="story">
    <p>Sourced from the beautiful<br>Coromandel Peninsula</p>
    <p>Our honey comes to your raw &amp;<br>unpasteurised, ensuring it retains<br>all the natural goodness!</p>
    <p>Arohanui,<br>Rowan, Noreen &amp; Boys</p>
    <p>‘Quillbrook’ –<br>all thanks to God for his<br>incredible creation!</p>
    <p class="contact">www.quillbrookhoney.co.nz<br>42 Tidewater Rd Whangamata<br>New Zealand</p>
  </div>

  <h1 class="brand brand-name">Quillbrook Honey Co.</h1>
  <h2 class="brand honey-type">Marram<br>Glade Honey</h2>
  <p class="brand net-weight">1KG</p>
  <p class="brand origin">WHANGAMATA N.Z.</p>

  <p class="facts claims">100% New Zealand Honey<br>No Added Ingredients</p>

  <div class="nutrition-panel">
    <h3 class="nutrition-title">NUTRITIONAL INFORMATION</h3>
    <div class="serving">Serving per package: 100<br>Serving size: 10g</div>
    <div class="rule rule-serving"></div>
    <div class="col col-head col-serving">Average<br>Quantity<br>per Serving</div>
    <div class="col col-head col-100g">Average<br>Quantity<br>per 100g</div>
    <div class="rule rule-heads"></div>
    <div class="col col-body col-label">Energy<br>Protein<br>Fat total<br>-saturated<br>Carbohydrate<br>-sugars<br>Sodium</div>
    <div class="col col-body col-serving">134kj<br>0.04g<br>0g<br>0g<br>7.9g<br>7.8g<br>1.2mg</div>
    <div class="col col-body col-100g">134kj<br>0.04g<br>0g<br>0g<br>79.6g<br>78.1g<br>1.2mg</div>
  </div>

  <p class="facts storage">Store upright in a cool, dry place.<br>No refrigeration needed.<br>Not recommended for infants below<br>the age of 12 months.</p>
</div>
</body>
</html>
```